Flyer-Design für Hundephysiopraxis
Zielgruppe
Ich bin selbstständige Hundephysiotherapeutin / Hundeosteopathin /Hundefitnesstrainerin. Meine Zielgruppe sind Hundehalter bzw. allgemein Tierhalter (biete noch weitere Dinge für Hunde/Tiere an) aber auch Tierärzte.
Aufgabenstellung
Es wäre schön, wenn Sie die Texte ähnlich wie auf meiner Homepage gestalten (z.B. Infos aus der Startseite oder Therapieformen).
Prinzipiell sollte es eher natürlich, freundlich und nett gestaltet sein. Schlichtere Farben passend zum Logo.
Homepage: www.pfotenwohlsein-muster.de
Bei den Maßen bin ich offen, hatte aber eher an diesen 'typischen Flyer' gedacht (3 seitiger Flyer mit Vorder und Rückseite) bin aber prinzipiell offen :)
Einen Beispiel Flyer habe ich drangehängt sowie z.B. schon ein paar Fotos die man ggf nutzen kann. Weitere Behandlunsfotos kann ich gerne nachreichen.
Die Flyer sollen hauptsächlich bei z.B. Tierärzten / Tierklinik / Tiernahrungsmärkte wie Napfkorb ausgelegt werden damit Menschen die mich noch nicht kennen auf meine Arbeit aufmerksam werden.

```html
<!DOCTYPE html>
<html lang="de">
<head>
<meta charset="utf-8">
<title>Pfotenwohlsein – Flyer</title>
<link href="https://fonts.googleapis.com/css2?family=Crimson+Text:wght@400;700&family=Sacramento&display=swap" rel="stylesheet">
<style>
:root{
  --navy:#1d5575;
  --deep:#174a68;
  --teal:#2f86a6;
  --cyan:#2eaac2;
  --aqua:#5cc3d3;
  --white:#ffffff;
  --ink:#2a4a5c;
  --orange:#d9772b;
  --page:#eef1f3;
  --photo-green:#6f8f4a;
  --photo-grass:#87a45a;
  --photo-skin:#c9a27f;
}
*{margin:0;padding:0;box-sizing:border-box}
html,body{width:1200px;height:999px;overflow:hidden;background:var(--page)}
body{font-family:"Crimson Text",Georgia,serif;color:var(--ink);position:relative}
.spread{position:absolute;left:260px;width:680px;height:478px;overflow:hidden;box-shadow:0 2px 10px rgba(0,0,0,.15)}
.spread--outside{top:12px;background:var(--navy)}
.spread--inside{top:505px;background:var(--white)}
.spread svg.shapes{position:absolute;inset:0;width:680px;height:478px}
.panel{position:absolute;top:0;width:227px;height:478px}
.p1{left:0}.p2{left:227px}.p3{left:454px;width:226px}
.abs{position:absolute}
.small{font-size:6.4px;line-height:1.3}
.white{color:var(--white)}
.intro{left:96px;top:8px;width:124px;font-size:6.6px;line-height:1.25;color:var(--white)}
.uses-title{left:12px;top:150px;font-size:8px;font-weight:700;color:var(--white)}
.uses{left:12px;top:166px;list-style:none;font-size:6.4px;line-height:1.45;color:var(--white)}
.offer{left:12px;top:370px;font-size:11.5px;line-height:1.3;color:var(--white)}
.quals{left:14px;top:8px;width:200px;text-align:center;font-size:4.9px;line-height:1.45;color:var(--white)}
.quals h3{font-size:6.2px;font-weight:700;margin-bottom:2px}
.quals p{margin-bottom:5px}
.contact{left:14px;top:232px;width:120px;font-size:4.9px;line-height:1.45;color:var(--white)}
.brand{left:0;top:18px;width:226px;text-align:center}
.brand-mark{width:38px;height:38px;border-radius:50%;border:2px solid var(--orange);margin:0 auto 3px}
.brand-name{font-size:12px;color:var(--orange);line-height:1.1}
.brand-sub{font-size:5.5px;color:var(--orange);letter-spacing:.5px}
.services{left:8px;top:338px;width:210px;text-align:center;font-size:9.4px;line-height:1.45;color:var(--white)}
.web{left:0;top:452px;width:226px;text-align:center;font-size:8.5px;color:var(--teal)}
.script{font-family:"Sacramento",cursive;color:var(--navy)}
.motto{left:22px;top:16px;width:190px;font-size:17px;line-height:1.05;transform:rotate(-8deg)}
.body-text{font-size:6.4px;line-height:1.3;text-align:justify}
.body-text p{margin-bottom:6px}
.t1{left:20px;top:100px;width:190px;color:var(--ink)}
.h2{font-weight:700;font-size:8.6px;line-height:1.2;color:var(--white)}
.h2a{left:14px;top:206px;width:200px}
.t2{left:14px;top:236px;width:200px;color:var(--white)}
.quote{left:30px;top:420px;width:175px;text-align:center;font-size:12px;line-height:1;color:var(--navy)}
.h3{left:10px;top:14px;width:206px;text-align:center}
.t3{left:12px;top:42px;width:202px;color:var(--white)}
</style>
</head>
<body>

<!-- Außenseite -->
<section class="spread spread--outside">
  <svg class="shapes" viewBox="0 0 680 478" aria-hidden="true">
    <path d="M0 0H90C95 30 85 60 70 75C50 90 20 85 0 82Z" fill="var(--teal)"/>
    <path d="M170 90C200 80 227 110 227 140V260C205 250 190 220 180 190C165 150 150 110 170 90Z" fill="var(--teal)" opacity=".7"/>
    <path d="M227 0H454V478H227Z" fill="var(--teal)"/>
    <path d="M227 0H454V300C420 290 380 310 340 300C300 290 260 260 227 270Z" fill="var(--navy)" opacity=".35"/>
    <path d="M454 0H680V478H454Z" fill="var(--white)"/>
    <path d="M470 100C500 70 560 80 600 90C650 100 672 140 668 190C664 250 650 300 620 330H470C455 260 450 150 470 100Z" fill="var(--aqua)" opacity=".5"/>
    <path d="M454 330C500 318 560 336 610 322C640 314 665 318 680 322V440H454Z" fill="var(--navy)"/>
    <g fill="var(--cyan)">
      <circle cx="204" cy="16" r="6"/><circle cx="197" cy="7" r="2.2"/><circle cx="204" cy="5" r="2.2"/><circle cx="211" cy="7" r="2.2"/>
      <circle cx="118" cy="138" r="6"/><circle cx="111" cy="129" r="2.2"/><circle cx="118" cy="127" r="2.2"/><circle cx="125" cy="129" r="2.2"/>
      <circle cx="640" cy="30" r="7"/><circle cx="632" cy="20" r="2.5"/><circle cx="640" cy="17" r="2.5"/><circle cx="648" cy="20" r="2.5"/>
      <circle cx="420" cy="262" r="7"/><circle cx="412" cy="252" r="2.5"/><circle cx="420" cy="249" r="2.5"/><circle cx="428" cy="252" r="2.5"/>
      <circle cx="428" cy="385" r="7"/><circle cx="420" cy="375" r="2.5"/><circle cx="428" cy="372" r="2.5"/><circle cx="436" cy="375" r="2.5"/>
    </g>
  </svg>
  <div class="abs" role="img" aria-label="Foto: Therapeutin behandelt einen Hund" style="left:0;top:0;width:84px;height:74px;border-radius:0 0 40px 0;background:linear-gradient(135deg,var(--photo-skin),#7d6a58)"></div>
  <div class="abs" role="img" aria-label="Foto: Therapeutin mit Spaniel auf der Wiese" style="left:240px;top:318px;width:180px;height:150px;border-radius:60px 40px 10px 50px;background:linear-gradient(160deg,var(--photo-grass),var(--photo-green) 60%,#4d6233)"></div>
  <div class="abs" role="img" aria-label="Foto: sitzender Spaniel auf der Wiese" style="left:490px;top:105px;width:150px;height:215px;border-radius:70px 50px 60px 40px;background:linear-gradient(170deg,#9bb06c,#4b4b48 45%,var(--photo-green))"></div>

  <div class="panel p1">
    <p class="abs intro">Für mich steht Dein Hund an erster Stelle! Ich habe selbst Erfahrungen mit Tierschutzhunden, sowie Hunden aus deutscher Zucht und weiß, dass manche Hunde „ihr Päckchen“ zu tragen haben. Umso mehr möchte ich, dass sich Dein Vierbeiner bei mir wohlfühlt, er mir Vertrauen schenkt und gerne zur Physiotherapie geht.</p>
    <h2 class="abs uses-title">Einsatzmöglichkeiten der Physiotherapie:</h2>
    <ul class="abs uses">
      <li>- Schmerzlinderung</li><li>- Muskelaufbau</li><li>- Koordinationsschulung</li><li>- Konditionsaufbau</li>
      <li>- Verbesserung der Beweglichkeit (Sehnen, Bänder - und Gelenke)</li><li>- Lösen von Blockaden</li><li>- Prävention</li>
      <li>- Gangschulung</li><li>- Nachsorge nach Operationen</li><li>- Wundheilungsstörungen</li><li>- Muskelverspannungen</li>
      <li>- neurologische Erkrankungen</li><li>- degenerative Erkrankungen</li>
    </ul>
    <p class="abs offer">Hundephysiotherapie<br>Hundeosteopathie<br>Dorn Therapie und Breuß Massage<br>Hundefitnesstrainer</p>
  </div>

  <div class="panel p2">
    <div class="abs quals">
      <h3>Meine Qualifikationen</h3>
      <p>Ausbildungen<br>Frühjahr 2020 erfolgreich beendete Ausbildung zur Hundephysiotherapeutin<br>Frühjahr 2022 erfolgreich beendete Ausbildung zur Hundeosteopathin</p>
      <p>Voraussichtliche Beendigung:<br>Sommer 2022 Hundefitnesstrainerin</p>
      <p>Seminare und Fortbildungen<br>Frühjahr 2021 Edelsteintherapie<br>Sommer 2021 Dorn Therapie in Kombination mit Breuß Massage<br>Sommer 2021 Tierkommunikation und Bachblüten<br>Frühjahr 2022 Blutegeltherapie in der Tierarztpraxis</p>
      <p>Weitere Abend- oder Wochenendseminare wie z.B. zu Gangbild, Ernährung und Erster Hilfe am Hund</p>
    </div>
    <div class="abs contact">
      <strong>Kontakt</strong><br>www.pfotenwohlsein-muster.de<br>E-Mail: hallo@pfotenwohlsein-muster.de<br>Handy: 0151 23456789<br>Termine nach Absprache<br>Anschrift: Wiesenweg 12, 12345 Musterstadt
    </div>
  </div>

  <div class="panel p3">
    <div class="abs brand">
      <div class="brand-mark"></div>
      <div class="brand-name">Pfotenwohlsein</div>
      <div class="brand-sub">Hundephysiotherapie · Lena Muster</div>
    </div>
    <p class="abs services">Hundephysiotherapie • Hundeosteopathie<br>Hundefitnesstrainerin • Bachblütenberaterin<br>Tierkommunikation • Mykotherapie<br>Edelsteintherapie</p>
    <p class="abs web">www.pfotenwohlsein-muster.de</p>
  </div>
</section>

<!-- Innenseite -->
<section class="spread spread--inside">
  <svg class="shapes" viewBox="0 0 680 478" aria-hidden="true">
    <path d="M0 300C40 280 90 300 130 290C170 280 200 300 227 296V478H0Z" fill="var(--teal)" opacity=".25"/>
    <path d="M227 0H454V478H227Z" fill="var(--navy)"/>
    <path d="M227 0H454V190C400 200 340 180 290 195C260 204 240 200 227 196Z" fill="var(--teal)"/>
    <path d="M454 0H680V478H454Z" fill="var(--navy)"/>
    <path d="M454 330C500 320 560 340 620 326C650 318 670 322 680 326V478H454Z" fill="var(--teal)"/>
    <g fill="var(--cyan)">
      <circle cx="185" cy="78" r="7"/><circle cx="177" cy="68" r="2.5"/><circle cx="185" cy="65" r="2.5"/><circle cx="193" cy="68" r="2.5"/>
      <circle cx="40" cy="455" r="7"/><circle cx="32" cy="445" r="2.5"/><circle cx="40" cy="442" r="2.5"/><circle cx="48" cy="445" r="2.5"/>
      <circle cx="430" cy="168" r="6"/><circle cx="423" cy="159" r="2.2"/><circle cx="430" cy="157" r="2.2"/><circle cx="437" cy="159" r="2.2"/>
      <circle cx="440" cy="392" r="7"/><circle cx="432" cy="382" r="2.5"/><circle cx="440" cy="379" r="2.5"/><circle cx="448" cy="382" r="2.5"/>
    </g>
  </svg>
  <div class="abs" role="img" aria-label="Foto: rennender schwarz-weißer Hund" style="left:40px;top:312px;width:160px;height:158px;border-radius:50% 45% 40% 50%;background:linear-gradient(160deg,#b9b9b0,#6d7a55 70%)"></div>
  <div class="abs" role="img" aria-label="Foto: Spaniel im Porträt" style="left:250px;top:6px;width:160px;height:150px;border-radius:40px 60px 50px 30px;background:linear-gradient(150deg,#8a6a4c,#d8d2c8 55%,#6c5a48)"></div>
  <div class="abs" role="img" aria-label="Foto: Therapeutin behandelt Spaniel auf der Wiese" style="left:470px;top:340px;width:200px;height:132px;border-radius:50px 40px 20px 60px;background:linear-gradient(160deg,var(--photo-grass),var(--photo-green) 60%,#4d6233)"></div>

  <div class="panel p1">
    <p class="abs script motto">Leben ist Bewegung und Bewegung ist Lebensqualität</p>
    <div class="abs body-text t1">
      <p>Rennen, laufen, springen, toben und spielen zeigt die Lebensfreude unserer Hunde! Wer keine Schmerzen hat, kann sich frei bewegen und hat Spaß dabei. Wenn unsere Hunde jedoch erkranken oder alt werden, dann benötigen sie unsere Unterstützung.</p>
      <p>Nach einem Unfall, bei Schmerzen oder Beschwerden im Rücken und in den Gelenken, nach Operationen oder bei Lahmheiten können Physiotherapie sowie Osteopathie helfen. Es lindert die Schmerzen, lockert verspannte Muskulatur, verbessert die Beweglichkeit oder stellt diese wiederher. Weiterhin baut Physiotherapie Muskulatur auf, fördert die Genesung und hilft im Alter fit zu bleiben.</p>
      <p>Ich helfe Deinem Hund gerne dabei, die Gesundheit und damit die Lebensqualität und Lebensfreude zurück zu erhalten.</p>
    </div>
  </div>

  <div class="panel p2">
    <h2 class="abs h2 h2a">Doch nicht nur die Hundephysiotherapie verhilft Deinem Hund zu mehr Vitalität …</h2>
    <div class="abs body-text t2">
      <p>Ist Dein Hund ängstlich? Ihm geht es nicht gut oder Du weißt aus verschiedenen Verhaltensweisen nicht weiter?</p>
      <p>Hier greift zum Beispiel die Tierkommunikation oder Bachblüten. Auch die Vitalpilz-Therapie wird in dem Veterinärbereich immer wichtiger, da hier grandiose Erfolge erzielt werden, u.a. bei Verdauungsproblemen, Immunstörungen, Allergie, Arthrose, Durchblutungsstörungen und sogar Krebs und Mittelmeerkrankheiten.</p>
      <p>Ist Dein Hund gesund, Du möchtest nur seine Fitness verbessern oder ein paar Kilos sollen schmelzen?</p>
      <p>Hier unterstütze ich Dich gerne mit meinen Hundefitnesstrainer Kenntnissen. Wir erstellen gemeinsam einen Trainingsplan für Deinen Hund heraus. Sei es für den Sporthund in Agility oder für die Couchpotato.</p>
    </div>
    <p class="abs script quote">„Lebensfreude lässt sich am besten von Hunden lernen“</p>
  </div>

  <div class="panel p3">
    <h2 class="abs h2 h3">Hundephysiotherapie &amp; Hundeosteopathie</h2>
    <div class="abs body-text t3">
      <p>In der Humanmedizin wird die Physiotherapie bei der Genesung der Patienten schon selbstverständlich und unterstützend eingesetzt. Tiere können an ähnlichen Problemen leiden wie wir Menschen. Sie haben genau so Schmerzen und dies schränkt ihr Leben ebenfalls ein. Wir können unsere Schmerzen äußern. Viele Hunde jedoch leben mit diesen Schmerzen viele Wochen, da er unauffällig wird und sie lahmen oder andere Dinge anzeigen. Gerade deshalb ist die Physiotherapie so enorm wichtig, damit unsere Hunde unbeschwert und ohne Schmerzen lange an unserer Seite bleiben.</p>
      <p>Jeder Körper ist ein individuelles und komplexes System mit eigenen Anforderungen an Bewegungsapparat, Intensitäten und Erholungsphasen. Entsprechend umfangreich aufgestellt ist das Therapiespektrum meiner Arbeit. Dabei immer im Fokus: Die stets vollkommen individuellen Therapieprogramme, in enger Zusammenarbeit mit dem Tierarzt, sensibel abgestimmt auf die spezifischen Anforderungen der einzelnen Krankheitsbilder. Jeder Hund hat eine andere Hintergrundgeschichte und auch dies berücksichtige ich bei meinen Therapien. Mein Ziel ist es, die Lebensfreude und Lebensqualität unserer Vierbeiner zu erhalten oder gar zu verbessern.</p>
    </div>
  </div>
</section>

</body>
</html>
```